Wordpress Design Project for Bin Hire company

Kestrel Skip Rentals is a Bin Hire company based in the Western Suburbs of Melbourne (Australia) and was established in 1995.
The colours of the Kestrel Skip Rentals logo are Pantone 188C (Burgundy) and 424C (Grey). We would like the site to include these colours throughout the site.

The current Kestrel Skip Rentals site (www.kestrelskiprentals-example.com.au) has been in operation for a number of years and as we have recently commenced a project to update the Logo and Corporate ID, a new Website is also appropriate.

The Kestrel Skip Rentals site only needs to be a simple site and is unlikely to consist of more than 20 pages. The site is primarily used for people to find our contact details, delivery areas and the measurements/size of of the bins we hire to our customers.

Industry/Entity Type

It Company

Requirements
Must have
• A contact page template (which sends an email) which can be used for a main contact page as well as long form response pages to enhance our 'call to action'
A separate enquiry/order form with configurable options will also be required.
A category (products) page will be required which will list all of our bins, a configurable excerpt of the page contents along with a single photo of each bin (a slider may be used also).
We also require the ability for potential customers to look each bin on it's own page as well as a large image, information about each bin and our terms and conditions.
We would also like configurable titles and meta code for each page.
The site will also need the ability to integrate with Tallyworth Metrics.

```html
<!DOCTYPE html>
<html lang="en">
<head>
<meta charset="utf-8">
<title>Kestrel Skip Rentals</title>
<link href="https://fonts.googleapis.com/css2?family=PT+Sans+Narrow:wght@400;700&family=PT+Sans:wght@400;700&display=swap" rel="stylesheet">
<style>
:root{
  --burgundy:#8e1510;
  --burgundy-dark:#260a09;
  --red-band:#b8342a;
  --red-band-deep:#9e2419;
  --grey-text:#8a8a8a;
  --grey-head:#8d8d8d;
  --link:#8e1510;
  --footer-link:#e0463a;
  --page-bg:#e2e2e2;
  --white:#ffffff;
}
*{margin:0;padding:0;box-sizing:border-box}
html,body{width:1168px;height:1200px;overflow:hidden}
body{position:relative;background:var(--page-bg);font-family:"PT Sans",sans-serif;color:var(--grey-text)}
.abs{position:absolute}
.site-header{left:0;top:0;width:1168px;height:107px;background:var(--white)}
.header-rule{left:156px;top:0;width:862px;height:7px;background:var(--burgundy)}
.brand{left:157px;top:24px;width:140px;font-family:"PT Sans Narrow",sans-serif;font-weight:700;font-size:29px;line-height:30px;color:var(--burgundy);text-transform:uppercase;letter-spacing:-0.5px}
.contact-block{font-size:12px;line-height:17.5px;color:var(--grey-text);letter-spacing:.2px}
.address{left:633px;top:39px}
.phone-labels{left:840px;top:39px}
.phone-values{left:897px;top:39px}
.icon{position:absolute}
.hero-band{left:0;top:107px;width:1168px;height:433px;background:linear-gradient(180deg,var(--red-band) 0%,#c23a2e 45%,var(--red-band-deep) 100%)}
.hero-frame{left:155px;top:145px;width:863px;height:306px;background:#a8291f;border:1px solid #7d1a13;box-shadow:0 0 6px rgba(0,0,0,.35)}
.hero-photo{left:166px;top:156px;width:616px;height:284px;background:linear-gradient(100deg,#3d3f36 0%,#5d5f4e 30%,#8b8a3a 55%,#c9a42c 70%,#3f8a4f 88%,#2b3a2c 100%)}
.hero-panel{left:782px;top:156px;width:225px;height:284px;background:linear-gradient(180deg,#111 0%,#1e1e1e 100%)}
.hero-title{left:802px;top:169px;font-family:"PT Sans Narrow",sans-serif;font-weight:700;font-size:33px;line-height:35px;color:#f2f2f2;letter-spacing:2px;text-transform:uppercase}
.hero-rule{left:802px;top:314px;width:191px;height:1px;background:#9a9a9a}
.hero-text{left:802px;top:323px;width:200px;font-size:12.5px;line-height:14.7px;color:#f2f2f2;letter-spacing:.3px}
.hero-button{left:801px;top:393px;width:191px;height:36px;background:linear-gradient(180deg,#c5271c,#8b130d);border:1px solid #4a0a06;box-shadow:0 2px 3px rgba(0,0,0,.5);font-family:"PT Sans Narrow",sans-serif;font-weight:700;font-size:16px;letter-spacing:1.5px;color:#fff;text-align:center;line-height:34px;text-transform:uppercase}
.main-nav{left:155px;top:485px;width:863px;height:55px;background:var(--burgundy-dark);border-radius:6px 6px 0 0}
.main-nav a{position:absolute;top:18px;font-family:"PT Sans Narrow",sans-serif;font-size:15px;color:#f4f4f4;text-decoration:none;letter-spacing:.5px}
.main-nav a.current{color:var(--footer-link)}
.content{left:156px;top:540px;width:862px;height:407px;background:var(--white)}
.section-title{font-family:"PT Sans Narrow",sans-serif;font-weight:700;font-size:20px;color:var(--grey-head);letter-spacing:.8px}
.dots{height:2px;background-image:radial-gradient(circle,#b5b5b5 0.8px,transparent 1px);background-size:5px 2px}
.body-copy{font-size:12.5px;line-height:17.3px;color:var(--grey-text);letter-spacing:.2px}
.body-copy p+p{margin-top:9px}
.read-more{color:var(--link);text-decoration:none}
.map{left:810px;top:606px;width:183px;height:265px;background:linear-gradient(160deg,#e8e2cf 0%,#ddd6bf 55%,#a9c6dd 85%,#9ec0da 100%)}
.site-footer{left:156px;top:947px;width:862px;height:181px;background:var(--burgundy-dark);border-radius:0 0 6px 6px}
.footer-nav a{position:absolute;left:184px;font-family:"PT Sans Narrow",sans-serif;font-size:15px;color:#f4f4f4;text-decoration:none;letter-spacing:.6px}
.footer-nav a.current{color:var(--footer-link)}
.footer-head{font-family:"PT Sans Narrow",sans-serif;font-size:15px;color:#f4f4f4;letter-spacing:.4px}
.product-link{position:absolute;font-size:12px;color:var(--footer-link);text-decoration:none;letter-spacing:.3px}
.footer-brand{left:780px;top:1005px;width:100px;font-family:"PT Sans Narrow",sans-serif;font-weight:700;font-size:17px;line-height:17px;color:#9a9a9a;text-transform:uppercase}
.copyright{font-size:12px;color:var(--footer-link);letter-spacing:.3px}
.footer-address{left:782px;top:1065px;font-size:11px;font-weight:700;color:#f4f4f4;letter-spacing:.2px}
</style>
</head>
<body>
<header class="site-header abs">
  <div class="header-rule abs"></div>
  <div class="brand abs">Kestrel Skip Rentals</div>
  <svg class="icon" style="left:598px;top:39px" width="24" height="32" viewBox="0 0 24 32" aria-hidden="true">
    <path d="M12 1C6 1 2 5.5 2 11c0 7.5 10 20 10 20s10-12.5 10-20C22 5.5 18 1 12 1z" fill="#c0261b"/>
    <circle cx="12" cy="11" r="4" fill="#fff"/>
  </svg>
  <div class="contact-block address abs">18 Harlow Lane<br>Seaholme Vic 3018</div>
  <svg class="icon" style="left:784px;top:40px" width="46" height="30" viewBox="0 0 46 30" aria-hidden="true">
    <path d="M4 10c0-6 38-6 38 0v4h-9v-3H13v3H4z" fill="#c0261b"/>
    <path d="M9 14h28l4 14H5z" fill="#d9342a"/>
    <circle cx="23" cy="20" r="5" fill="#f3d3cf"/>
  </svg>
  <div class="contact-block phone-labels abs">Phone:<br>E-mail:</div>
  <div class="contact-block phone-values abs">03 9000 4821<br>hello@kestrel.example</div>
</header>

<section class="hero-band abs"></section>
<div class="hero-frame abs"></div>
<div class="hero-photo abs" role="img" aria-label="Photo of a row of wheelie bins with red, yellow and green lids"></div>
<div class="hero-panel abs"></div>
<h1 class="hero-title abs">Supplying<br>domestic &amp;<br>commercial<br>walk in bins</h1>
<div class="hero-rule abs"></div>
<p class="hero-text abs">We deliver walk in bins in the western suburbs of Melbourne and over the Westgate Bridge to South Melbourne.</p>
<a class="hero-button abs">Find out more</a>

<nav class="main-nav abs">
  <a class="current" style="left:29px">Home</a>
  <a style="left:123px">About Us</a>
  <a style="left:228px">Product List</a>
  <a style="left:348px">Delivery Area</a>
  <a style="left:473px">Contact Us</a>
</nav>

<main class="content abs"></main>
<h2 class="section-title abs" style="left:185px;top:563px">About our Company</h2>
<div class="dots abs" style="left:181px;top:591px;width:577px"></div>
<div class="body-copy abs" style="left:183px;top:598px;width:580px">
  <p>Kestrel Skip Rentals has been delivering bins in the western suburbs of Melbourne and over the Westgate Bridge to South Melbourne since 1999.</p>
  <p>We supply walk in bins for domestic and commercial use. Our bins range in size from 4 cubic metres through to 10 cubic metres. We also have 20 cubic metre bins. All bins have gates for easy access and most will fit in a standard driveway. &nbsp;<a class="read-more">read more &gt;</a></p>
</div>

<h2 class="section-title abs" style="left:185px;top:732px">We make it easy for you</h2>
<div class="dots abs" style="left:181px;top:757px;width:266px"></div>
<div class="body-copy abs" style="left:185px;top:767px;width:270px">
  <p>A Council permit is required for bins placed outside your property i.e. on the road, nature strip or in a laneway/ROW. We will apply to Council for a permit on your behalf. Please call us for current permit rates for your area.</p>
  <p style="margin-top:6px"><a class="read-more">read more &gt;</a></p>
</div>

<h2 class="section-title abs" style="left:502px;top:732px">Our Products</h2>
<div class="dots abs" style="left:498px;top:757px;width:262px"></div>
<div class="body-copy abs" style="left:499px;top:767px;width:266px">
  <p>A Council permit is required for bins placed outside your property i.e. on the road, nature strip or in a laneway/ROW. We will apply to Council for a permit on your behalf. Please call us for current permit rates for your area.</p>
  <p style="margin-top:6px"><a class="read-more">read more &gt;</a></p>
</div>

<h2 class="section-title abs" style="left:809px;top:562px">Where we deliver</h2>
<div class="dots abs" style="left:809px;top:591px;width:184px"></div>
<div class="map abs" role="img" aria-label="Street map of Melbourne's western suburbs showing the delivery area"></div>

<footer class="site-footer abs"></footer>
<nav class="footer-nav">
  <a class="current" style="top:976px">Home</a>
  <a style="top:1007px">About Us</a>
  <a style="top:1038px">Delivery Area</a>
  <a style="top:1069px">Contact Us</a>
</nav>
<div class="footer-head abs" style="left:362px;top:976px">Products</div>
<a class="product-link" style="left:362px;top:1009px">4 cubic metre walk in bin</a>
<a class="product-link" style="left:525px;top:1009px">10 cubic metre walk in bin</a>
<a class="product-link" style="left:362px;top:1040px">6 cubic metre walk in bin</a>
<a class="product-link" style="left:525px;top:1040px">20 cubic metre walk in bin</a>
<a class="product-link" style="left:362px;top:1071px">8 cubic metre walk in bin</a>
<a class="product-link" style="left:525px;top:1071px">read more &gt;</a>
<div class="footer-head abs" style="left:780px;top:976px">Legal</div>
<div class="footer-brand abs">Kestrel Skip Rentals</div>
<div class="copyright abs" style="left:888px;top:1005px">© 2012</div>
<div class="copyright abs" style="left:888px;top:1036px">All rights reserved</div>
<div class="footer-address abs">18 Harlow Lane Seaholme Vic 3018</div>
</body>
</html>
```